Business cards for a recruitment company
Marrowby Associates
Modern
Helena Marrowby
Managing Director
PO Box 48213 Corvel Harbour Plaza Dubai United Arab Emirates
lena@marrowbyassociates-mail.test
marrowbyassociates-mail.test
The business card needs to have my name, designation etc in both English and Arabic. Therefore, both languages will appear on the front of the card. The final design will illustrate how two different translations will appear on the front of the card. **The logo must also appear on the front of the card.
The back of the card will be plain white with just the logo as attached in the AI file. Perhaps the logo could be indented.

```html
<!DOCTYPE html>
<html lang="en">
<head>
<meta charset="utf-8">
<title>Marrowby Associates – Business Cards</title>
<link rel="stylesheet" href="https://fonts.googleapis.com/css2?family=Montserrat:wght@400;500;600&family=Cairo:wght@600;700&display=swap">
<style>
  :root {
    --backdrop: #e9e7ec;
    --card-black: #141215;
    --card-white: #ffffff;
    --accent-purple: #9a7bb8;
    --text-light: #f2f0f4;
    --text-muted: #b9b3bf;
    --text-dark: #1c1a1e;
    --rule: #5a5360;
  }
  * { box-sizing: border-box; margin: 0; padding: 0; }
  html, body {
    width: 1200px; height: 797px; overflow: hidden;
    background: var(--backdrop);
    font-family: "Montserrat", Arial, sans-serif;
  }
  .sheet {
    position: relative; width: 1200px; height: 797px;
    display: flex; align-items: center; justify-content: center; gap: 40px;
  }
  .card {
    position: relative; width: 540px; height: 310px;
    overflow: hidden; border-radius: 4px;
    box-shadow: 0 10px 30px rgba(0,0,0,0.18);
  }
  .card-shape { position: absolute; inset: 0; width: 100%; height: 100%; }

  /* Front */
  .card-front { background: var(--card-black); color: var(--text-light); }
  .holder { position: absolute; left: 34px; top: 40px; }
  .holder-name {
    color: var(--accent-purple); font-size: 17px; font-weight: 600;
    letter-spacing: 2.5px; text-transform: uppercase;
  }
  .holder-title { margin-top: 6px; font-size: 11.5px; color: var(--text-muted); letter-spacing: 0.5px; }
  .holder-rule { margin-top: 12px; width: 290px; height: 1px; background: var(--rule); }
  .contacts { position: absolute; left: 34px; top: 140px; list-style: none; }
  .contact-item {
    display: flex; align-items: center; gap: 10px;
    font-size: 11px; color: var(--text-light); margin-bottom: 12px; letter-spacing: 0.3px;
  }
  .contact-icon { width: 16px; height: 16px; flex: none; }
  .holder-arabic {
    position: absolute; right: 150px; top: 118px; text-align: right; direction: rtl;
    font-family: "Cairo", Arial, sans-serif; color: var(--text-light);
  }
  .arabic-name { font-size: 25px; font-weight: 700; line-height: 1.3; }
  .arabic-title { font-size: 17px; font-weight: 600; color: var(--text-muted); }

  /* Brand lockup */
  .brand {
    position: absolute; display: flex; align-items: center; gap: 10px;
  }
  .brand-dot { width: 18px; height: 18px; border-radius: 50%; background: var(--accent-purple); flex: none; }
  .brand-name {
    font-size: 13px; font-weight: 500; letter-spacing: 3px; text-transform: uppercase;
    color: var(--text-dark); line-height: 1.5;
  }
  .card-front .brand { right: 22px; bottom: 34px; width: 120px; }
  .card-front .brand-name { font-size: 10px; letter-spacing: 2px; }

  /* Back */
  .card-back { background: var(--card-white); }
  .card-back .brand { left: 90px; top: 122px; gap: 14px; }
  .card-back .brand-dot { width: 30px; height: 30px; }
  .card-back .brand-name { font-size: 20px; letter-spacing: 4px; }
  .back-web {
    position: absolute; right: 20px; bottom: 30px;
    font-size: 9.5px; color: var(--text-light); letter-spacing: 0.5px;
  }
</style>
</head>
<body>
<main class="sheet">

  <section class="card card-front" aria-label="Card front">
    <svg class="card-shape" viewBox="0 0 540 310" aria-hidden="true">
      <path d="M370 310 C 380 190, 450 95, 540 70 L540 310 Z" fill="var(--card-white)"/>
    </svg>

    <div class="holder">
      <p class="holder-name">Helena Marrowby</p>
      <p class="holder-title">Managing Director</p>
      <div class="holder-rule"></div>
    </div>

    <ul class="contacts">
      <li class="contact-item">
        <svg class="contact-icon" viewBox="0 0 16 16" aria-hidden="true">
          <circle cx="8" cy="8" r="8" fill="var(--accent-purple)"/>
          <path d="M5.4 4.2c.4-.3.9-.2 1.1.2l.6 1.2c.2.3.1.7-.2.9l-.5.4c.4.9 1.1 1.6 2 2l.4-.5c.2-.3.6-.4.9-.2l1.2.6c.4.2.5.7.2 1.1l-.5.6c-.4.4-1 .5-1.5.3C7.2 10 6 8.8 5.1 6.9c-.2-.5-.1-1.1.3-1.5z" fill="var(--card-black)"/>
        </svg>
        014 552 7308
      </li>
      <li class="contact-item">
        <svg class="contact-icon" viewBox="0 0 16 16" aria-hidden="true">
          <circle cx="8" cy="8" r="8" fill="var(--accent-purple)"/>
          <rect x="4" y="5.2" width="8" height="5.6" rx="0.6" fill="none" stroke="var(--card-black)" stroke-width="1"/>
          <path d="M4.3 5.6 8 8.4l3.7-2.8" fill="none" stroke="var(--card-black)" stroke-width="1"/>
        </svg>
        lena@marrowbyassociates-mail.test
      </li>
      <li class="contact-item">
        <svg class="contact-icon" viewBox="0 0 16 16" aria-hidden="true">
          <circle cx="8" cy="8" r="8" fill="var(--accent-purple)"/>
          <circle cx="8" cy="8" r="3.8" fill="none" stroke="var(--card-black)" stroke-width="1"/>
          <path d="M4.2 8h7.6M8 4.2c-1.4 1.2-1.4 6.4 0 7.6M8 4.2c1.4 1.2 1.4 6.4 0 7.6" fill="none" stroke="var(--card-black)" stroke-width="0.9"/>
        </svg>
        marrowbyassociates-mail.test
      </li>
    </ul>

    <div class="holder-arabic" lang="ar">
      <p class="arabic-name">هيلينا ماروبي</p>
      <p class="arabic-title">المدير العام</p>
    </div>

    <div class="brand">
      <span class="brand-dot"></span>
      <span class="brand-name">Marrowby Associates</span>
    </div>
  </section>

  <section class="card card-back" aria-label="Card back">
    <svg class="card-shape" viewBox="0 0 540 310" aria-hidden="true">
      <path d="M370 310 C 380 190, 450 95, 540 70 L540 310 Z" fill="var(--card-black)"/>
    </svg>

    <div class="brand">
      <span class="brand-dot"></span>
      <span class="brand-name">Marrowby<br>Associates</span>
    </div>

    <p class="back-web">marrowbyassociates-mail.test</p>
  </section>

</main>
</body>
</html>
```